Digital Marketing Consultant Needs a Business Card Design

I need a business card to brand myself - I'm a digital marketing consultant, and I do web design, SEO, lead generation, social media, etc. I'm overhauling my website (CorinneHalvorsk.com) and just had a snazzy new logo made.

I like the combo of yellow & gray - I find it eye-catching, upbeat and techie. The exact colors of yellow and gray that I like are #F6BF27 and #6D6D6D. But I'm open to suggestions and other color combinations!

I plan on printing the card using some high-end printing techniques that will ensure the card stands out - either really thick cards with colored edges, or spot UV. Not sure which yet, so if you want to incorporate that into your design, that'd be great!

I'm looking for a clean and modern design, but something that will really stand out when paired with 'fancy' printing.

Target Market(s)

Small and medium-sized business owners.

Industry/Entity Type

Printing

Contact Information for Business Card

Corinne Halvorsk
Digital Marketing
Call or Text: 850-555-0927
Corinne@CorinneHalvorsk.com
www.CorinneHalvorsk.com
@QPZ47 on Twitter

Font styles to use
Serif
Sans Serif

Requirements
Must have
• My logo, my contact information, and my "company colors" - #F6BF27 and #6D6D6D.
Nice to have
• If there's room to mention all the things that I do:
• Social Media, Web Design, SEO, Lead Generation, Conversion Funnels, PPC
• (don't add if it makes the card cluttered)

```html
<!DOCTYPE html>
<html lang="en">
<head>
<meta charset="utf-8">
<title>Corinne Halvorsk – Business Card</title>
<link rel="stylesheet" href="https://fonts.googleapis.com/css2?family=Cinzel:wght@500&family=Exo+2:wght@400;600&display=swap">
<style>
  :root {
    --page-bg: #e9e7e4;
    --card-white: #ffffff;
    --card-shade: #f1f1f1;
    --brand-yellow: #F6BF27;
    --swoosh-yellow: #fdd15a;
    --brand-gray: #6D6D6D;
    --band-gray: #a9a9a9;
    --text-dark: #2b2b2b;
    --text-mid: #4a4a4a;
  }
  * { margin: 0; padding: 0; box-sizing: border-box; }
  html, body { width: 1200px; height: 900px; overflow: hidden; }
  body {
    background: var(--page-bg);
    display: flex;
    align-items: center;
    justify-content: center;
    font-family: "Exo 2", sans-serif;
  }
  .card {
    position: relative;
    width: 1000px;
    height: 570px;
    background: linear-gradient(135deg, var(--card-white) 0%, var(--card-shade) 100%);
    box-shadow: 0 10px 30px rgba(0,0,0,0.15);
    overflow: hidden;
  }
  .card-waves { position: absolute; inset: 0; }
  .brand {
    position: absolute;
    left: 110px;
    top: 255px;
    display: flex;
    align-items: center;
    gap: 14px;
    white-space: nowrap;
  }
  .brand-square {
    flex: none;
    width: 34px;
    height: 34px;
    border: 3px solid var(--brand-gray);
  }
  .brand-name {
    font-family: "Cinzel", serif;
    font-weight: 500;
    font-size: 26px;
    letter-spacing: 1.5px;
    color: var(--brand-gray);
    text-transform: uppercase;
  }
  .divider {
    position: absolute;
    left: 568px;
    top: 70px;
    width: 3px;
    height: 250px;
    background: var(--brand-yellow);
  }
  .contact {
    position: absolute;
    left: 595px;
    top: 72px;
    color: var(--text-mid);
  }
  .contact-name {
    font-weight: 600;
    font-size: 25px;
    letter-spacing: 1px;
    color: var(--text-dark);
    text-transform: uppercase;
  }
  .contact-title { font-size: 17px; margin-top: 2px; }
  .contact-address { font-size: 17px; line-height: 1.3; margin-top: 18px; }
  .contact-list { list-style: none; margin-top: 26px; font-size: 15px; letter-spacing: 1px; }
  .contact-list li { display: flex; align-items: center; gap: 12px; height: 27px; }
  .contact-list svg { width: 16px; height: 16px; fill: var(--text-dark); }
  .website {
    position: absolute;
    right: 40px;
    bottom: 150px;
    font-size: 21px;
    letter-spacing: 1px;
    color: var(--card-white);
  }
</style>
</head>
<body>
  <main class="card">
    <svg class="card-waves" viewBox="0 0 1000 570" preserveAspectRatio="none" aria-hidden="true">
      <path fill="var(--band-gray)" d="M0,495 C300,525 560,470 720,375 C820,318 900,298 1000,285 L1000,570 L0,570 Z"/>
      <path fill="var(--swoosh-yellow)" d="M0,452 C260,500 560,450 735,325 C590,470 280,505 0,474 Z"/>
    </svg>

    <div class="brand">
      <span class="brand-square"></span>
      <span class="brand-name">Corinne Halvorsk</span>
    </div>

    <div class="divider"></div>

    <section class="contact">
      <h1 class="contact-name">Marcus Delvane</h1>
      <p class="contact-title">Managing Director</p>
      <p class="contact-address">027.9th floor Plaza<br>Harbor Road KLM</p>
      <ul class="contact-list">
        <li>
          <svg viewBox="0 0 24 24"><path d="M6.6 10.8a15 15 0 0 0 6.6 6.6l2.2-2.2c.3-.3.7-.4 1-.2 1.1.4 2.3.6 3.6.6.6 0 1 .4 1 1V20c0 .6-.4 1-1 1A17 17 0 0 1 3 4c0-.6.4-1 1-1h3.5c.6 0 1 .4 1 1 0 1.3.2 2.5.6 3.6.1.3 0 .7-.2 1z"/></svg>
          012 555 0143
        </li>
        <li>
          <svg viewBox="0 0 24 24"><path d="M7 1h10a2 2 0 0 1 2 2v18a2 2 0 0 1-2 2H7a2 2 0 0 1-2-2V3a2 2 0 0 1 2-2zm0 3v14h10V4zm5 15.5a1 1 0 1 0 0 2 1 1 0 0 0 0-2z"/></svg>
          012 555 0143
        </li>
        <li>
          <svg viewBox="0 0 24 24"><path d="M6 2h9l3 3v4h2a2 2 0 0 1 2 2v10H2V11a2 2 0 0 1 2-2h2zm2 2v5h8V6h-2V4zm-2 9v2h3v-2zm5 0v2h3v-2zm5 0v2h3v-2z"/></svg>
          012 555 0143
        </li>
        <li>
          <svg viewBox="0 0 24 24"><path d="M2 5h20v14H2zm2 2v.5l8 5.5 8-5.5V7z"/></svg>
          yourname@mailbox.com
        </li>
      </ul>
    </section>

    <p class="website">www.yoursitename.com</p>
  </main>
</body>
</html>
```